I would like some help creating my first business cards for my new business, I am a facilitator of a course that I have created. I am currently starting the sales promotion and marketing part of my business and need some help designing the business cards. Something fairly simple would be good, the core theme of my work is in connection of women to themselves and to each other. My initial design is a tree lit up by lights, a very mother earth type of image. This is not my design however so I probably am not legally able to use the design. I don't have a logo. Could you possibly assist with this?

I would really like to have the following details on the business card:
Mel Harbison
0431 582 904
hi.mel.harbison@quillpost.example

And also the image

Target Market(s)

Women who are living in an isolated environment

Industry/Entity Type

Counsellor

Contact Information for Business Card

Mel Harbison
Facilitator
hi.mel.harbison@quillpost.example
0431 582 904

Font styles to use
Other font styles liked:
• Handwriting - Dakota

Colors
e34197
fee18a
3276b5
33a6d7
33b8a4

Requirements
Must have
• 1) My details as above
• 2) a design (picture) that represents the mother earth theme similar to the designs included in the brief
• 3) no copyright attached to the design
• 4) Colours are very important but it is difficult to describe the colour using the colour wheel. Please refer to the example of the tree that I have included in the drop box.
• 5) I must apologise that I forgot to add the business card needs to have the name of the business in gold letters please: Riverstone Circle for Ladies, thank you
Nice to have
• It would be great to use the tree design that I included in the brief, this is my favourite picture but I think it is probably copyrighted. If it's not, that is the one I would like on my business cards please.

```html
<!DOCTYPE html>
<html lang="en">
<head>
<meta charset="utf-8">
<title>Mel Harbison – Business Card</title>
<link href="https://fonts.googleapis.com/css2?family=Open+Sans:wght@400;700&family=Great+Vibes&display=swap" rel="stylesheet">
<style>
  :root {
    --page-bg: #bfe3d8;
    --sky-top: #a9dcf5;
    --sky-glow: #ffffff;
    --earth: #6b4a26;
    --gold: #c08a22;
    --name-brown: #5a3d1e;
    --muted-grey: #7d7d7d;
    --contact-ink: #4a3a2a;
  }
  html, body {
    margin: 0;
    padding: 0;
    width: 1200px;
    height: 856px;
    overflow: hidden;
    background: var(--page-bg);
  }
  .card {
    position: absolute;
    left: 100px;
    top: 142px;
    width: 1000px;
    height: 572px;
    border-radius: 48px;
    overflow: hidden;
    background: radial-gradient(ellipse 55% 60% at 64% 46%, var(--sky-glow) 0%, #e6f6fd 40%, var(--sky-top) 100%);
    box-shadow: 0 8px 24px rgba(40, 90, 80, 0.18);
  }
  .tree-art {
    position: absolute;
    left: 50px;
    top: 90px;
    width: 460px;
    height: 430px;
    background: radial-gradient(closest-side at 50% 48%, #f7b84a 0%, #f29a3a 35%, #b9d97a 65%, rgba(185, 217, 122, 0.4) 82%, rgba(173, 214, 240, 0) 100%);
  }
  .earth-band {
    position: absolute;
    left: 0;
    bottom: 0;
    width: 1000px;
    height: 140px;
  }
  .holder {
    position: absolute;
    right: 78px;
    top: 44px;
    text-align: right;
    font-family: "Open Sans", sans-serif;
  }
  .holder-name {
    margin: 0;
    font-size: 34px;
    font-weight: 700;
    color: var(--name-brown);
    line-height: 1.05;
  }
  .holder-role {
    margin: 0;
    font-size: 22px;
    font-weight: 400;
    color: var(--muted-grey);
    line-height: 1.1;
  }
  .business-name {
    position: absolute;
    left: 500px;
    top: 128px;
    width: 420px;
    margin: 0;
    text-align: center;
    font-family: "Great Vibes", cursive;
    font-weight: 400;
    font-size: 70px;
    line-height: 0.95;
    color: var(--gold);
  }
  .contacts {
    position: absolute;
    right: 60px;
    top: 398px;
    display: flex;
    gap: 18px;
    align-items: center;
    font-family: "Open Sans", sans-serif;
    font-size: 21px;
    color: var(--contact-ink);
  }
  .contact-item {
    display: flex;
    align-items: center;
    gap: 8px;
  }
  .contact-icon {
    width: 22px;
    height: 22px;
    flex: none;
  }
</style>
</head>
<body>
  <main class="card">
    <div class="tree-art" role="img" aria-label="Illustration of a brown tree with a colourful crown of swirling rings, stars and flowers"></div>

    <svg class="earth-band" viewBox="0 0 1000 140" preserveAspectRatio="none" role="img" aria-label="Brown grassy ground silhouette">
      <path d="M0 140 L0 118 C200 104 420 86 640 66 C790 52 900 40 1000 28 L1000 140 Z" fill="var(--earth)"/>
    </svg>

    <header class="holder">
      <p class="holder-name">Mel Harbison</p>
      <p class="holder-role">Facilitator</p>
    </header>

    <h1 class="business-name">Riverstone<br>Circle for<br>Ladies</h1>

    <div class="contacts">
      <span class="contact-item">
        <svg class="contact-icon" viewBox="0 0 24 24" aria-hidden="true">
          <circle cx="12" cy="12" r="11" fill="var(--contact-ink)"/>
          <path d="M7 10 Q12 6 17 10 L15.5 11.5 L14 10.5 L10 10.5 L8.5 11.5 Z M8 13 H16 V17 H8 Z" fill="#fff"/>
        </svg>
        0431 582 904
      </span>
      <span class="contact-item">
        <svg class="contact-icon" viewBox="0 0 24 24" aria-hidden="true">
          <circle cx="12" cy="12" r="11" fill="var(--contact-ink)"/>
          <rect x="6" y="8" width="12" height="8" fill="#fff"/>
          <path d="M6 8 L12 13 L18 8" fill="none" stroke="var(--contact-ink)" stroke-width="1.3"/>
        </svg>
        hi.mel.harbison@quillpost.example
      </span>
    </div>
  </main>
</body>
</html>
```